Logo & Visitenkarte für Coach
Zielgruppe
Was:
Sie haben eine Idee und wir coach Sie bei der Umsetzung.
Wer:
Alle Unternehmen oder Privatperson mit einer Idee.
Aufgabenstellung
Als Anhang sende ich Ihnen ein paar Bilder von einem Stein. Es geht mir nicht um die Farbgebung sondern nur um die 4 Flächen dieses Steines.
Meine Firma berut auf drei Säulen, der Stein hat eine Grundfläche lila und drei Flächen in pink, Wissen, Liebe und Glaube.

```html
<!DOCTYPE html>
<html lang="de">
<head>
<meta charset="utf-8">
<title>Kernweg – Logo &amp; Visitenkarte</title>
<link rel="stylesheet" href="https://fonts.googleapis.com/css2?family=Open+Sans:wght@400;700&display=swap">
<style>
  :root {
    --bg: #ffffff;
    --ink: #4a4a4a;
    --ink-dark: #3f3f3f;
    --green: #2ea43a;
    --green-light: #8fd18f;
    --paper: #ffffff;
  }
  * { margin: 0; padding: 0; box-sizing: border-box; }
  html, body { width: 1200px; height: 675px; overflow: hidden; background: var(--bg); }
  body { font-family: "Open Sans", Arial, sans-serif; color: var(--ink); }

  .canvas { position: relative; width: 1200px; height: 675px; }

  .card {
    position: absolute; width: 480px; height: 300px;
    background: var(--paper); overflow: hidden;
    box-shadow: 0 6px 18px rgba(0,0,0,.16);
  }
  .card__bg { position: absolute; inset: 0; width: 100%; height: 100%; }

  .brand { display: flex; align-items: center; gap: 12px; }
  .brand__dot { border-radius: 50%; background: var(--green-light); flex: none; }
  .brand__name { font-weight: 700; color: var(--ink); letter-spacing: .04em; line-height: 1; }

  .logo-block { position: absolute; left: 60px; top: 400px; }
  .logo-block .brand__dot { width: 90px; height: 90px; }
  .logo-block .brand__name { font-size: 62px; }

  .card--front { left: 400px; top: 40px; }
  .card--front .brand { position: absolute; left: 50%; top: 50%; transform: translate(-50%, -58%); }
  .card--front .brand__dot { width: 44px; height: 44px; }
  .card--front .brand__name { font-size: 38px; }

  .card--back { left: 680px; top: 340px; }
  .card--back .brand { position: absolute; left: 26px; top: 26px; gap: 7px; }
  .card--back .brand__dot { width: 20px; height: 20px; }
  .card--back .brand__name { font-size: 17px; }

  .portrait {
    position: absolute; left: 50px; top: 92px; width: 150px; height: 208px;
    border-radius: 75px 75px 0 0;
    background: linear-gradient(180deg, #e9e6e3 0%, #c9c3bd 28%, #2b2f3d 46%, #1f2330 100%);
  }

  .contact {
    position: absolute; right: 28px; top: 34px; text-align: right;
    color: #fff; font-size: 11px; line-height: 1.55;
  }
  .contact__name { font-weight: 700; font-size: 15px; margin-bottom: 8px; }
  .contact__block + .contact__block { margin-top: 10px; }

  .claim {
    position: absolute; right: 14px; bottom: 11px;
    font-size: 9px; font-weight: 700; color: var(--ink-dark); white-space: nowrap;
  }
</style>
</head>
<body>
<main class="canvas">

  <section class="card card--front" aria-label="Visitenkarte Vorderseite">
    <svg class="card__bg" viewBox="0 0 480 300" aria-hidden="true">
      <path d="M0 0 H480 V8 C320 10 160 16 0 28 Z" fill="var(--ink)"/>
      <path d="M0 300 V262 C150 262 330 252 480 200 V300 Z" fill="var(--green)"/>
      <path d="M0 268 C150 268 330 258 480 206" fill="none" stroke="var(--paper)" stroke-width="6"/>
    </svg>
    <div class="brand">
      <span class="brand__dot"></span>
      <span class="brand__name">KERNWEG</span>
    </div>
  </section>

  <section class="card card--back" aria-label="Visitenkarte Rückseite">
    <svg class="card__bg" viewBox="0 0 480 300" aria-hidden="true">
      <rect width="480" height="300" fill="var(--ink)"/>
      <rect x="0" y="258" width="480" height="42" fill="var(--green)"/>
      <path d="M0 0 H120 C200 50 235 170 215 300 H0 Z" fill="var(--paper)"/>
      <path d="M120 0 C200 50 235 170 215 300" fill="none" stroke="var(--green)" stroke-width="9"/>
    </svg>
    <div class="brand">
      <span class="brand__dot"></span>
      <span class="brand__name">KERNWEG</span>
    </div>
    <div class="portrait" role="img" aria-label="Porträtfoto eines Coaches im dunklen Anzug mit verschränkten Armen"></div>
    <div class="contact">
      <p class="contact__name">Lena Beispiel</p>
      <div class="contact__block">
        <p>Ideencoach</p>
        <p>Beispielweg 7</p>
        <p>54321 Neustadt</p>
      </div>
      <div class="contact__block">
        <p>Tel.: 0987 / 654321</p>
        <p>info@kernweg-demo.de</p>
        <p>www.kernweg-demo.de</p>
      </div>
    </div>
    <p class="claim">Gute Ideen wachsen, wenn man sie gemeinsam angeht.</p>
  </section>

  <div class="logo-block">
    <div class="brand">
      <span class="brand__dot"></span>
      <span class="brand__name">KERNWEG</span>
    </div>
  </div>

</main>
</body>
</html>
```